Letterhead for Midwest Law Firm

Our law firm does estate planning and trust administration in Wisconsin and Illinois. We recently obtained a new logo and need to incorporate it into new stationary. The stationary needs to list out the attorneys at the firm, but we will want 3 variations, one with three attorneys, one with six, and one with six plus the names of states where each is licensed to practice (possibly as an asterisk with notation somewhere towards bottom of page. As with most traditional law practices, letterhead should be conservative and convey predictability and reliability. We view our brand as being primarily reliability, with prestige as a secondary element. We are upmarket, but would like to avoid seeming pretentious or "slick". We are a smaller firm with a personal touch.

Target Market(s)

Affluent Midwestern Americans approaching at or approaching retirement age.

Industry/Entity Type

Legal

Font styles to use
Serif
Sans Serif

Requirements
Must have
• Must use our logo. Must comply with Northgate Counsel Guild Ethics rules: https://www.quarvenlex.org/rules/offices/docs/plmtk41annotated.pdf. Must be conventional. Must list names of attorneys and provide contact information for firm. Note that we are asking for three designs with very minor variations. Also, designer must provide letterhead in a format that is industry-standard for stationary printers.
Nice to have
• We would appreciate an alternate version that will look reasonable when printed on a black-and-white printer. Designer can use judgment as to whether to have use grayscale, black/white, or something in between.
Should not have
• No "motto" or "visit our website" extraneous materials. putting the website address somewhere is fine, but overall there is a lot of required text, and we'd like to not appear cluttered.

```html
<!DOCTYPE html>
<html lang="en">
<head>
<meta charset="utf-8">
<title>Hollister &amp; Crane LLP — Letterhead</title>
<link href="https://fonts.googleapis.com/css2?family=Fira+Sans:wght@400;500&display=swap" rel="stylesheet">
<style>
  :root {
    --backdrop: #d9d9da;
    --paper: #fbfbfb;
    --ink: #2b2b2e;
    --navy: #1f2447;
    --gold: #efa927;
    --sky: #1a9ad8;
    --signature-blue: #3a63b8;
  }
  html, body {
    margin: 0;
    width: 1200px;
    height: 1200px;
    overflow: hidden;
    background: var(--backdrop);
    font-family: "Fira Sans", Arial, sans-serif;
    color: var(--ink);
  }
  .letterhead {
    position: absolute;
    left: 215px;
    top: 50px;
    width: 770px;
    height: 1100px;
    background: var(--paper);
    box-shadow: 0 6px 24px rgba(0,0,0,0.12);
    overflow: hidden;
  }
  .firm-mark {
    position: absolute;
    left: 50px;
    top: 62px;
    display: flex;
    align-items: center;
    gap: 10px;
  }
  .firm-mark__dot {
    width: 22px;
    height: 22px;
    border-radius: 50%;
    background: var(--gold);
  }
  .firm-mark__name {
    font-size: 20px;
    font-weight: 500;
    color: var(--navy);
    letter-spacing: 0.2px;
  }
  .firm-contact {
    position: absolute;
    right: 50px;
    top: 58px;
    font-size: 12px;
    line-height: 17px;
    color: var(--ink);
  }
  .firm-contact__line {
    display: flex;
    align-items: center;
    gap: 5px;
  }
  .firm-contact__line svg { width: 11px; height: 11px; }
  .letter {
    position: absolute;
    left: 168px;
    top: 318px;
    width: 520px;
    font-size: 15px;
    line-height: 25px;
  }
  .letter__recipient { margin: 0 0 28px; }
  .letter__body { margin: 0 0 28px; text-align: justify; }
  .letter__closing { margin: 40px 0 6px; }
  .letter__signature {
    width: 240px;
    height: 46px;
    background: linear-gradient(90deg, rgba(58,99,184,0.18), rgba(58,99,184,0.08));
    border-radius: 4px;
  }
  .footer-band {
    position: absolute;
    left: 0;
    bottom: 0;
    width: 770px;
    height: 40px;
  }
</style>
</head>
<body>
  <main class="letterhead">
    <header>
      <div class="firm-mark">
        <span class="firm-mark__dot"></span>
        <span class="firm-mark__name">Hollister &amp; Crane LLP</span>
      </div>
      <address class="firm-contact" style="font-style:normal">
        <div>218 E. Larkmoor Avenue</div>
        <div>Suite 310, Brenton</div>
        <div>WI 53990</div>
        <div class="firm-contact__line">
          <svg viewBox="0 0 12 12" aria-hidden="true"><path d="M2.5 1h2l1 2.5-1.3 1a6 6 0 0 0 3.3 3.3l1-1.3L11 7.5v2a1 1 0 0 1-1 1A9 9 0 0 1 1.5 2a1 1 0 0 1 1-1z" fill="var(--sky)"/></svg>
          555-214-9200
        </div>
        <div class="firm-contact__line">
          <svg viewBox="0 0 12 12" aria-hidden="true"><rect x="3" y="1" width="6" height="3" fill="none" stroke="var(--sky)"/><rect x="1" y="4" width="10" height="5" rx="1" fill="none" stroke="var(--sky)"/><rect x="3" y="7" width="6" height="4" fill="var(--paper)" stroke="var(--sky)"/></svg>
          555-214-0664
        </div>
      </address>
    </header>

    <section class="letter">
      <p class="letter__recipient">To<br>The,<br>Director</p>
      <p class="letter__body">Lorem ipsum dolor sit amet, consectetur adipiscing elit. Sed at ante. Mauris eleifend, quam a vulptate dictum, massa quam dapibus leo, eget vulputate orci purus ut lorem. In fringilla mi in ligula. Pellen tesque aliquam quam vel dolor. Nunc adipiscing. Sed quamodio, tempus ac, aliquam molestie varius ac, tellus. Vestibulum ut nulla aliquam risus rutrum interdum. Pellentesque lorem.</p>
      <p class="letter__body">Curabitur sit amet erat quis risus feugiat viverra. Pellentesque augue justo,sagittis et, lacinia at, venenatis non, arcu. Nunc nec libero. In cursus dictum risus. Etiam tristique nisl a nulla.</p>
      <p class="letter__closing">Thanking you,</p>
      <div class="letter__signature" role="img" aria-label="Handwritten signature of Walter J. Hollister"></div>
    </section>

    <svg class="footer-band" viewBox="0 0 770 40" aria-hidden="true">
      <polygon points="0,8 560,8 592,40 0,40" fill="var(--gold)"/>
      <polygon points="580,20 770,20 770,40 600,40" fill="var(--sky)"/>
    </svg>
  </main>
</body>
</html>
```